Business Card for Restaurant Vendal

This project consist of creating 2 design for business card of restaurant named Vendal.

The attached specs below are 'ONLY SUGGESTION' if you have others ideas. You are welcome to post it.

1) Restaurant Card

Adresse:
2784 Côte du Pinard Vert
Montréal (Qc) H4K 3T8

Website:
www.ven-dal.ca

Phone:
438-719-2046

2) Employee Card

Name: Lorna Pik
Title: Owner

Address:
2784 Côte du Pinard Vert
Montréal (Qc) H4K 3T8

Email:lorna@ven-dal.ca
Phone Number:438-719-2046
Cellphone Number:514-830-4162

 The attached specs are 'ONLY SUGGESTION' if you have others ideas.  You are welcome to post it.

Industry/Entity Type

Restaurant

Requirements
Must have
• UV Card Spot

To print Spot UV business cards you would have to submit 2 files for each side. The first file "base" would be your regular design file as it would have been in any other case. The 2nd file "UV mask" is a black/white file. The BLACK color will indicate the areas that will be covered with the UV high gloss finish. To upload the files, please combine front design and front mask file in one P
Nice to have
• 1) The font of the logo should be ink effect
2) black background with wallpaper effect
3) The specs below are 'ONLY SUGGESTION' if you have others ideas. You are welcome to post it.

```html
<!DOCTYPE html>
<html lang="fr">
<head>
<meta charset="utf-8">
<title>Vendal – Cartes d'affaires</title>
<link href="https://fonts.googleapis.com/css2?family=Questrial&family=Noto+Sans+JP:wght@400&display=swap" rel="stylesheet">
<style>
  :root {
    --page: #e9e7e4;
    --ink: #141313;
    --ink-soft: #221f1f;
    --paper: #ffffff;
    --text-dark: #2a2a2a;
    --text-grey: #6c6c6c;
    --white: #f4f4f4;
    --red: #e0281c;
    --lantern-grey: #9a9a9a;
  }
  * { box-sizing: border-box; margin: 0; padding: 0; }
  html, body { width: 1200px; height: 873px; overflow: hidden; }
  body {
    background: var(--page);
    font-family: "Questrial", "Century Gothic", sans-serif;
    display: flex;
    align-items: center;
    justify-content: center;
    gap: 60px;
  }
  .card {
    position: relative;
    width: 510px;
    height: 300px;
    overflow: hidden;
    box-shadow: 0 6px 18px rgba(0,0,0,.18);
  }

  /* Front */
  .card--front {
    background:
      repeating-linear-gradient(90deg, rgba(255,255,255,.025) 0 1px, transparent 1px 4px),
      linear-gradient(160deg, var(--ink-soft), var(--ink));
    color: var(--white);
  }
  .front__lantern {
    position: absolute;
    left: -20px;
    bottom: -30px;
    width: 200px;
    height: 230px;
    border-radius: 48% 48% 44% 44%;
    background: radial-gradient(circle at 40% 40%, #bdbdbd, var(--lantern-grey) 45%, rgba(80,80,80,.4) 75%, transparent 100%);
    opacity: .85;
  }
  .front__brand {
    position: absolute;
    left: 210px;
    top: 88px;
    display: flex;
    flex-direction: column;
    align-items: flex-start;
  }
  .brand-name {
    display: flex;
    align-items: center;
    gap: 12px;
    font-size: 66px;
    line-height: 1;
    letter-spacing: 1px;
    color: var(--white);
  }
  .brand-name__dot {
    width: 12px;
    height: 12px;
    border-radius: 50%;
    background: var(--red);
  }
  .front__tagline {
    margin-top: 14px;
    font-size: 13px;
    letter-spacing: .5px;
    color: var(--white);
  }
  .front__tagline .sep { color: var(--red); margin: 0 4px; }

  /* Back */
  .card--back {
    background: var(--paper);
    color: var(--text-dark);
    padding: 30px 34px;
  }
  .back__kana {
    font-family: "Noto Sans JP", sans-serif;
    font-size: 30px;
    color: var(--text-dark);
    margin-bottom: 26px;
  }
  .back__details {
    list-style: none;
    font-size: 13px;
    line-height: 1.45;
    color: var(--text-grey);
  }
  .back__details li + li { margin-top: 10px; }
  .back__lantern {
    position: absolute;
    right: 34px;
    top: 60px;
    width: 140px;
    height: 200px;
  }
</style>
</head>
<body>

  <section class="card card--front" aria-label="Recto de la carte">
    <div class="front__lantern" role="img" aria-label="Lanterne japonaise en papier, illustration grise"></div>
    <div class="front__brand">
      <h1 class="brand-name"><span class="brand-name__dot" aria-hidden="true"></span>Vendal</h1>
      <p class="front__tagline">Resto-Bar Japonais<span class="sep">•</span>Izakaya</p>
    </div>
  </section>

  <section class="card card--back" aria-label="Verso de la carte">
    <p class="back__kana" lang="ja">ヴェンダル</p>
    <ul class="back__details">
      <li>2784 Côte du Pinard Vert<br>Montréal (Qc) H4K 3T8</li>
      <li>(514) 438-719-2046</li>
      <li>www.ven-dal.ca</li>
      <li>info@ven-dal.ca</li>
    </ul>
    <svg class="back__lantern" viewBox="0 0 140 200" role="img" aria-label="Lanterne rouge d'izakaya, illustration">
      <ellipse cx="70" cy="118" rx="56" ry="74" fill="var(--red)"/>
    </svg>
  </section>

</body>
</html>
```